Brevant Engineering needs an A4 flyer (2 sides)

Brevant Engineering is an Australian Owned and Operated business offering 1) metallurgical consulting service and 2) tooling supplier to Australia's manufacturing industry. The purpose of this flyer is to portray the business to its audience as an 'Japanese Quality' Tool Supplier backed by a metallurgical expert, who knows what it takes to manufacture high performance precision tools. With over 20 years experience as a metallurgist, i have come across hundreds of problems (failures) related to steel and tools that prompted me to start a tool making business. Making tools that out last ordinary tools. Our tools are of superior quality, performance and price competitive to Australian made tools because they are made by a Japanese Owned Tool making company, who supplies Japan. All our tools are made with Only Japanese Tool Steel from well known brands such as Kosen, Tamari, Morioka. Our products include: Extrusion Die, Stamping Die, Forming Die, Forging Die, Customised Tools and Components.
The purpose of the flyer is catch attention of the production manager, engineering manager and tooling manager as "Why should i consider doing business with you?", why should i trust your tools?

Target Market(s)

Australian manufacturers associating with Aluminium Extrusion, Metal Products, Plastic extrusion, PVC extrusion and Sheet Metal Industry

Industry/Entity Type

Metal Stamping

Font styles to use
Sans Serif

Colors

Designer to choose colors to be used in the design.

Requirements
Must have
• Australian Owned & Operated (front page)
Genuine Japanese Quality (Tools & Dies)
Japanese Tool Steel
Kosen, Tamari, Morioka (Steels)
Nice to have
• Please use photos provided and read existing brochure to get some depth and nature of the business and technical capacity. Any suggestion or request of photos is welcome, please email me.
Should not have
• Not sure at this stage

```html
<!DOCTYPE html>
<html lang="en">
<head>
<meta charset="utf-8">
<title>Brevant Engineering – A4 Flyer</title>
<link rel="stylesheet" href="https://fonts.googleapis.com/css2?family=Montserrat:wght@400;500;700&family=Sarabun:wght@400;500;700&display=swap">
<style>
  :root{
    --bg:#e4e4e6;
    --teal:#46a9bb;
    --teal-deep:#3a95a6;
    --slate:#6c6c6e;
    --slate-dark:#4a4a4c;
    --ink:#2e3033;
    --paper:#ffffff;
    --mist:#eef0f1;
    --logo-grey:#8a8b8d;
  }
  *{margin:0;padding:0;box-sizing:border-box}
  html,body{width:1200px;height:902px;overflow:hidden;background:var(--bg)}
  body{position:relative;font-family:"Sarabun",sans-serif;color:var(--ink)}

  .page{position:absolute;top:93px;width:508px;height:716px;background:var(--paper);overflow:hidden;box-shadow:2px 3px 6px rgba(0,0,0,.28)}
  .page--front{left:74px}
  .page--back{left:616px}
  .page-label{position:absolute;top:831px;font-size:12.5px;color:var(--slate);transform:translateX(-50%)}
  .abs{position:absolute}
  .shapes{position:absolute;left:0;top:0}

  /* brand name block */
  .brand{position:absolute;font-family:"Montserrat",sans-serif;font-weight:700;color:var(--logo-grey);text-align:center;line-height:1.05;letter-spacing:.5px}
  .brand__mark{display:block;margin:0 auto 6px;background:var(--logo-grey)}

  /* FRONT */
  .front-brand{left:350px;top:52px;width:140px;font-size:17px}
  .front-brand .brand__mark{width:34px;height:34px}
  .headline{position:absolute;left:43px;top:150px;font-family:"Montserrat",sans-serif;font-weight:400;font-size:24.5px;line-height:31px;color:var(--ink)}
  .hero-photo{position:absolute;left:0;top:0;width:508px;height:716px;
    clip-path:polygon(0 341px,508px 238px,508px 716px,0 716px);
    background:linear-gradient(110deg,#3c4654 0%,#6f7b86 30%,#c9d2d8 55%,#8b98a4 80%,#5d6c7a 100%)}
  .hero-tint{position:absolute;left:0;top:563px;width:508px;height:153px;background:var(--teal);opacity:.92}
  .thumb{position:absolute;top:517px;width:101px;height:87px;border:1px solid rgba(255,255,255,.85)}
  .thumb__img{position:absolute;left:5px;top:5px;right:5px;bottom:5px}
  .thumb--1{left:37px}.thumb--1 .thumb__img{background:linear-gradient(160deg,#d9d3c8,#4a4540)}
  .thumb--2{left:149px}.thumb--2 .thumb__img{background:linear-gradient(135deg,#c9a53c,#8a6a1c)}
  .thumb--3{left:260px}.thumb--3 .thumb__img{background:linear-gradient(160deg,#9fb2c8,#232a36)}
  .thumb--4{left:372px}.thumb--4 .thumb__img{background:linear-gradient(135deg,#b8babc,#5b5e62)}
  .url-box{position:absolute;left:148px;top:640px;width:213px;height:25px;border:1px solid var(--paper);
    font-family:"Montserrat",sans-serif;font-weight:700;font-size:19px;line-height:23px;color:var(--paper);text-align:center}
  .tagline{position:absolute;left:0;width:508px;top:676px;text-align:center;font-family:"Montserrat",sans-serif;font-size:13px;color:var(--ink)}

  /* BACK */
  .back-mist{position:absolute;left:0;top:0;width:508px;height:238px;background:linear-gradient(120deg,#eceef0 0%,#f3f4f5 50%,#e0e3e6 100%)}
  .section-title{position:absolute;font-family:"Montserrat",sans-serif;font-weight:700;font-size:13px;color:var(--teal);letter-spacing:.3px}
  .body-copy{position:absolute;font-size:11.4px;line-height:15.9px;color:var(--ink)}
  .char-banner{position:absolute;left:149px;top:184px;width:228px;height:28px}
  .char-banner__text{position:absolute;left:0;top:0;width:228px;line-height:28px;text-align:center;font-family:"Montserrat",sans-serif;font-weight:700;font-size:14px;color:var(--paper);letter-spacing:.4px}
  .teal-panel{position:absolute;left:28px;top:199px;width:189px;height:407px;background:var(--teal)}
  .grey-panel{position:absolute;left:217px;top:238px;width:260px;height:368px;background:var(--mist)}
  .tab{position:absolute;left:17px;width:176px;height:17px;background:var(--slate);color:var(--paper);font-family:"Montserrat",sans-serif;font-weight:700;font-size:11.5px;line-height:17px;padding-left:21px;letter-spacing:.3px}
  .tab::after{content:"";position:absolute;left:0;top:17px;border-top:6px solid var(--slate-dark);border-left:11px solid transparent}
  .tab--steel{top:233px}
  .tab--products{top:466px}
  .steel-brands{position:absolute;left:43px;top:262px;display:grid;grid-template-columns:76px 80px;row-gap:4px;font-family:"Montserrat",sans-serif;font-weight:700;font-size:15.5px;color:var(--paper)}
  .steel-brands li{list-style:none;line-height:21px}
  .steel-brands li::before{content:"•";margin-right:4px}
  .feature-list{position:absolute;left:43px;list-style:none;font-size:10px;line-height:15.2px;color:var(--paper)}
  .feature-list li::before{content:"•";margin-right:7px}
  .feature-list--a{top:323px}
  .feature-list--b{top:391px}
  .product-list{position:absolute;left:35px;top:497px;width:180px;list-style:none;font-size:10px;line-height:12.6px;color:var(--paper)}
  .product-list li{padding-left:9px;position:relative;margin-bottom:4px}
  .product-list li::before{content:"•";position:absolute;left:0}
  .tile{position:absolute;border:1px solid #cfd2d4}
  .tile--a{left:228px;top:232px;width:111px;height:85px;background:linear-gradient(160deg,#f1f0ee,#5f5f5f)}
  .tile--b{left:352px;top:232px;width:111px;height:85px;background:linear-gradient(180deg,#e8e9ea,#45474a)}
  .tile--c{left:228px;top:359px;width:111px;height:85px;background:linear-gradient(160deg,#ffffff,#8a8d90)}
  .tile--d{left:352px;top:359px;width:111px;height:194px;background:linear-gradient(180deg,#a9b1b3 0%,#6e767a 45%,#c46a4a 70%,#8a9093 100%)}
  .tile--e{left:228px;top:467px;width:111px;height:86px;background:linear-gradient(160deg,#2ea0e6,#137bc8)}
  .caption{position:absolute;font-size:10px;line-height:12.4px;color:var(--teal)}
  .contact{position:absolute;top:645px;font-size:10px;line-height:12.4px;color:var(--ink)}
  .contact__key{color:var(--teal)}
  .divider{position:absolute;top:645px;width:1px;height:32px;background:var(--teal)}
  .back-brand{left:372px;top:618px;width:114px;font-size:14px}
  .back-brand .brand__mark{width:30px;height:30px}
</style>
</head>
<body>

<section class="page page--front" aria-label="Flyer front">
  <svg class="shapes" width="508" height="716" viewBox="0 0 508 716">
    <polygon points="0,0 246,0 0,46" fill="var(--teal)"/>
    <polygon points="0,46 246,0 0,61" fill="var(--slate)"/>
  </svg>

  <div class="brand front-brand"><span class="brand__mark"></span>BREVANT<br>ENGINEERING</div>

  <h1 class="headline">Tooling Design and<br>Manufacture Specialist<br>Metallurgical Solutions<br>Provider</h1>

  <div class="hero-photo" role="img" aria-label="Metallurgist examining a sample under a laboratory microscope"></div>
  <svg class="shapes" width="508" height="716" viewBox="0 0 508 716">
    <polygon points="0,341 508,238 508,254 0,343" fill="var(--slate)"/>
    <polygon points="0,343 508,254 508,268 0,348" fill="var(--teal)"/>
  </svg>
  <div class="hero-tint"></div>

  <div class="thumb thumb--1"><div class="thumb__img" role="img" aria-label="Hardness tester probe on a steel sample"></div></div>
  <div class="thumb thumb--2"><div class="thumb__img" role="img" aria-label="Gold-toned steel microstructure"></div></div>
  <div class="thumb thumb--3"><div class="thumb__img" role="img" aria-label="Coordinate measuring probe over a machined part"></div></div>
  <div class="thumb thumb--4"><div class="thumb__img" role="img" aria-label="Set of machined round die components"></div></div>

  <div class="url-box">www.brevant.com.au</div>
  <p class="tagline">Australian owned and operated</p>
</section>
<span class="page-label" style="left:328px">Front</span>

<section class="page page--back" aria-label="Flyer back">
  <div class="back-mist" role="img" aria-label="Faint workshop machinery backdrop"></div>
  <svg class="shapes" width="508" height="716" viewBox="0 0 508 716">
    <polygon points="374,0 508,0 508,33" fill="var(--slate)"/>
    <polygon points="400,0 508,0 508,22" fill="var(--teal)"/>
  </svg>

  <h2 class="section-title" style="left:28px;top:31px">WHO WE ARE...</h2>
  <p class="body-copy" style="left:28px;top:51px;width:205px">Brevant Engineering is a metallurgical consultant and a supplier of Japanese quality tools, molds and dies.</p>

  <h2 class="section-title" style="left:250px;top:35px">OUR OBJECTIVE...</h2>
  <p class="body-copy" style="left:250px;top:53px;width:205px">Is to work in partnership with you to optimize your tooling performance, reduce tooling cost and to achieve competitive products.</p>

  <h2 class="section-title" style="left:28px;top:114px">OUR REPUTATION...</h2>
  <p class="body-copy" style="left:28px;top:134px;width:440px">Brevant Engineering brings over 20 year of combined experience in Metallurgical R&amp;D, Product Development, Heat Treatment &amp; Tooling Project Management.</p>

  <div class="teal-panel"></div>
  <div class="grey-panel"></div>

  <div class="char-banner">
    <svg class="shapes" width="228" height="28" viewBox="0 0 228 28">
      <polygon points="0,14 8,0 228,0 220,14" fill="#8e8f91"/>
      <polygon points="14,28 6,0 206,0 214,28" fill="var(--slate-dark)"/>
      <polygon points="6,0 222,0 212,28 16,28" fill="var(--slate-dark)"/>
    </svg>
    <div class="char-banner__text">TOOL CHARACTERISICS</div>
  </div>

  <div class="tab tab--steel">SPECIALTY TOOL STEEL</div>
  <ul class="steel-brands">
    <li>Kosen</li><li>Tamari</li>
    <li>Morioka</li><li>Sakuragi</li>
  </ul>
  <ul class="feature-list feature-list--a">
    <li>Precision Engineering</li>
    <li>Vacuum Heat Treatment</li>
    <li>High toughness</li>
    <li>High fatigue strength</li>
  </ul>
  <ul class="feature-list feature-list--b">
    <li>Improve tool/die life</li>
    <li>Increase productivity</li>
    <li>Reduce tooling cost</li>
  </ul>

  <div class="tab tab--products">PRODUCTS &amp; SERVICES</div>
  <ul class="product-list">
    <li>Extrusion Dies – Aluminium, Plastic, Polymers</li>
    <li>Stamping Dies – Aluminium, Steel</li>
    <li>Assorted Tools – Precision parts, Punches, Cutters, dies etc..</li>
    <li>Metallurgical testings &amp; verifications</li>
  </ul>

  <div class="tile tile--a" role="img" aria-label="Customised assorted steel tools laid out on a bench"></div>
  <div class="tile tile--b" role="img" aria-label="Hardness testing machine with a steel bar"></div>
  <div class="tile tile--c" role="img" aria-label="Aluminium extrusion die sections"></div>
  <div class="tile tile--d" role="img" aria-label="Metal stamping die set with orange springs"></div>
  <div class="tile tile--e" role="img" aria-label="Aluminium stamping die model on blue"></div>

  <p class="caption" style="left:228px;top:321px">Customised Assorted Tools<br>(Hot &amp; Cold Applications)</p>
  <p class="caption" style="left:363px;top:321px">Metallurgical testings<br>&amp; verifications</p>
  <p class="caption" style="left:228px;top:449px">Extrusion Die - Aluminium</p>
  <p class="caption" style="left:228px;top:566px">Stamping Die – Aluminium<br>(photo needs cropping )</p>
  <p class="caption" style="left:363px;top:566px">Stamping Die - Metal</p>

  <p class="contact" style="left:30px"><span class="contact__key">P.</span> (03) 9010 4427<br><span class="contact__key">M.</span>&nbsp; 0400 318 206</p>
  <span class="divider" style="left:122px"></span>
  <p class="contact" style="left:134px"><span class="contact__key">E.</span>&nbsp; info@brevant.com.au<br><span class="contact__key">W.</span> www.brevant.com.au</p>
  <span class="divider" style="left:241px"></span>
  <p class="contact" style="left:252px">48 Kestrel Rd,<br>Oakvale VIC 3199,<br>Australia</p>

  <div class="brand back-brand"><span class="brand__mark"></span>BREVANT<br>ENGINEERING</div>

  <svg class="shapes" width="508" height="716" viewBox="0 0 508 716">
    <polygon points="0,673 170,716 0,716" fill="var(--slate)"/>
    <polygon points="0,683 150,716 0,716" fill="var(--teal)"/>
  </svg>
</section>
<span class="page-label" style="left:892px">Back</span>

</body>
</html>
```